QuillVex is a crypto-arbitrage tool that finds arbitrages between and within exchanges.A logo for the websiteA designer will need to design main page which will describe the project.A subscription page which will have subscription packages. A client portal page where client can set filter types, payment options etc...A Solutions page which will have the actual solutions which quillVex will calculate. Other pages that have to do with login and subscribing. We need all this to be done as a project with actual color numbers high quality images. ETRO... We have attached the current Mock up but designer should have their own input and make it better.
Updates
Project is large and people need time to get it done, please extend by 3 weeks
Need more time to get the project finished right
Target Market(s)
Crypto Traders that are looking to make more money trading
Industry/Entity Type
Finance
Coding
Coded - Design and coding required
Number of Pages Required
5+ page
Colors
Designer to choose colors to be used in the design.
Requirements
Nice to have
- Good animations

```html
<!DOCTYPE html>
<html lang="en">
<head>
<meta charset="utf-8">
<title>QuillVex – Client Filters &amp; Solutions</title>
<link rel="stylesheet" href="https://fonts.googleapis.com/css2?family=Montserrat:wght@400;500;600;700&display=swap">
<style>
:root{
  --blue:#1a8ad0;
  --orange:#f7901e;
  --orange-light:#fbb03b;
  --bg:#f3f7fb;
  --panel:#ffffff;
  --row-hl:#e2ecf6;
  --text:#2f3a45;
  --muted:#8a96a3;
  --line:#dde5ee;
  --footer:#2b2b2b;
  --footer-text:#cfd3d8;
}
*{box-sizing:border-box;margin:0;padding:0}
html,body{width:1200px;height:3673px;overflow:hidden}
body{font-family:"Montserrat",sans-serif;background:var(--bg);color:var(--text);position:relative;font-size:11px}
.abs{position:absolute}

.site-header{left:0;top:0;width:1200px;height:60px;background:var(--blue)}
.brand{left:78px;top:10px;font-size:30px;font-weight:500;color:#fff;letter-spacing:.5px}
.nav a{position:absolute;top:21px;color:#fff;text-decoration:none;font-size:12px;font-weight:500}
.nav .active{background:var(--orange);border-radius:14px;padding:5px 14px;top:16px}
.avatar{left:952px;top:10px;width:40px;height:40px;border-radius:50%;background:linear-gradient(#f2c8a8,#e07a55);border:2px solid #fff}
.user{left:1003px;top:16px;color:#fff;font-size:11px;font-weight:700;line-height:14px}
.user span{display:block;font-weight:500;font-size:9px}

.h-center{left:0;width:1200px;text-align:center;color:var(--blue);font-weight:600}
.h-small{font-size:14px;font-weight:700}
.h-step{font-size:22px}
.sub{left:0;width:1200px;text-align:center;font-size:11px}
.select{left:490px;top:160px;width:215px;height:28px;background:#fff;border:1px solid var(--line);border-radius:3px;font-size:10px;color:var(--muted);padding:7px 10px}
.select::after{content:"";position:absolute;right:12px;top:11px;border:4px solid transparent;border-top-color:var(--muted)}
.hint{font-size:11px}

.panel{background:var(--panel);box-shadow:0 2px 10px rgba(40,80,120,.12)}
.panel-title{background:var(--blue);color:#fff;font-weight:700;font-size:11px;height:24px;line-height:24px;padding-left:12px;margin:10px 8px 0}
.list{list-style:none;padding:10px 8px 0}
.list li{height:28px;line-height:28px;padding:0 12px;font-size:10px;display:flex;justify-content:space-between;align-items:center;text-transform:uppercase}
.list li.hl{background:var(--row-hl)}
.list li.dim{background:#eef1f4;color:#c4cbd3}
.nolimit{padding:6px 8px 0 8px;font-size:10px}
.toggle{width:22px;height:11px;border-radius:6px;background:var(--orange);position:relative}
.toggle::after{content:"";position:absolute;right:1px;top:1px;width:9px;height:9px;border-radius:50%;background:#fff}
.off{width:14px;height:14px;border-radius:50%;background:#eef2f6;color:#9aa6b2;font-size:9px;line-height:14px;text-align:center;text-transform:none;font-style:normal}
.arrow{color:var(--blue);font-size:20px;font-weight:700}

.btn{display:block;text-align:center;font-weight:700;font-size:11px;border-radius:16px;text-transform:uppercase}
.btn-primary{background:linear-gradient(90deg,var(--orange),var(--orange-light));color:#fff;box-shadow:0 4px 10px rgba(247,144,30,.35)}
.btn-ghost{border:1px solid var(--blue);color:var(--blue);border-radius:2px;background:#fff}
.divider{left:0;width:1200px;height:1px;background:#e4ebf2}

.mp-title{font-size:14px;font-weight:700;color:#1d3c66;text-align:center;margin-top:28px}
.slider{position:absolute;left:24px;right:24px;top:101px;height:8px;background:#dce6ef;border-radius:4px}
.slider i{position:absolute;left:0;top:0;height:8px;width:35%;border-radius:4px;background:linear-gradient(90deg,#2ba5d8,#f2c21b)}
.status{list-style:none;padding:14px 20px}
.status li{font-size:11px;margin-bottom:14px;display:flex;align-items:center;gap:10px}
.dot{width:12px;height:12px;border-radius:50%;border:3px solid #bfe1f5;background:var(--blue)}
.radio{font-size:10px;display:flex;align-items:center;gap:8px}

.sol-table{left:220px;top:2356px;width:760px;height:296px;padding:12px 10px}
table{border-collapse:collapse;width:100%}
th{background:var(--blue);color:#fff;font-size:10px;font-weight:700;text-align:left;height:24px;padding:0 10px}
td{font-size:10px;height:27.5px;padding:0 10px;white-space:nowrap}
tr.hl td{background:var(--row-hl)}
.det{display:inline-block;border:1px solid #c9d3dd;border-radius:10px;font-size:8px;font-weight:700;padding:3px 10px;color:#3a4a5a}
.det.on{background:var(--orange);border-color:var(--orange);color:#fff}
.chev{color:var(--blue)}

.detail{left:387px;top:2775px;width:429px;height:519px}
.mini{position:absolute;left:17px;width:392px;box-shadow:0 1px 6px rgba(40,80,120,.15);background:#fff}
.mini td{height:30px;font-size:9px;padding:0 8px}
.mini th{font-size:9px;height:20px;padding:0 8px}
.link{color:var(--blue);text-decoration:underline;font-size:8px}
.transfer{position:absolute;left:90px;width:253px;height:29px;border:1px solid var(--line);background:#fff;text-align:center;line-height:29px;font-size:12px}

.site-footer{left:0;top:3404px;width:1200px;height:228px;background:var(--footer);color:var(--footer-text)}
.fcol{position:absolute;top:58px}
.fcol h4{color:#fff;font-size:13px;font-weight:700;margin-bottom:14px}
.fcol li{list-style:none;font-size:11px;margin-bottom:10px}
.fcol li::before{content:"»";margin-right:8px}
.social li::before{content:none}
.social li{display:flex;align-items:center;gap:8px;margin-bottom:14px}
.social .sq{width:18px;height:18px;border-radius:50%;background:var(--blue)}
.social .sq.alt{background:#c9587a}
.flogo{left:906px;top:92px;font-size:34px;color:#fff;font-weight:400}
.bottom-bar{left:0;top:3632px;width:1200px;height:41px;background:#fff;font-size:10px}
.bottom-bar .l{position:absolute;left:147px;top:14px}
.bottom-bar .l b{color:var(--orange);font-weight:600}
.bottom-bar .r{position:absolute;right:147px;top:14px}
</style>
</head>
<body>

<header class="abs site-header">
  <div class="abs brand">QuillVex</div>
  <nav class="nav">
    <a class="active" style="left:568px">Solutions</a>
    <a style="left:690px">FAQ</a>
    <a style="left:762px">Help</a>
    <a style="left:830px">Community</a>
  </nav>
  <div class="abs avatar" role="img" aria-label="User profile photo"></div>
  <div class="abs user">Mara Lenn<span>QV01</span></div>
</header>

<h2 class="abs h-center h-small" style="top:130px">MY FILTERS</h2>
<div class="abs select">Search</div>

<h2 class="abs h-center h-step" style="top:258px">Step 1</h2>
<p class="abs hint" style="left:252px;top:314px">Please select your active exchanges</p>
<p class="abs hint" style="left:661px;top:314px">Please select your starting and ending exchanges</p>

<section class="abs panel" style="left:245px;top:343px;width:306px;height:392px">
  <div class="panel-title">EXCHANGE LIST</div>
  <ul class="list">
    <li class="hl">Zolvexa<i class="toggle"></i></li>
    <li>Kantriq<i class="off">x</i></li>
    <li>Bremlox<i class="toggle"></i></li>
    <li>Fentaro<i class="toggle"></i></li>
    <li>Yusken<i class="off">x</i></li>
    <li>Breminox<i class="toggle"></i></li>
    <li>Qorvila<i class="toggle"></i></li>
    <li>Vintoska<i class="off">x</i></li>
    <li>Yuskeno<i class="toggle"></i></li>
    <li>Dorvak24<i class="toggle"></i></li>
    <li>Yuskeno<i class="toggle"></i></li>
    <li>Nubravek<i class="off">x</i></li>
  </ul>
</section>
<div class="abs arrow" style="left:592px;top:402px">‹</div>
<div class="abs arrow" style="left:596px;top:438px">›</div>
<div class="abs arrow" style="left:592px;top:622px">‹</div>
<div class="abs arrow" style="left:596px;top:658px">›</div>

<section class="abs panel" style="left:649px;top:343px;width:301px;height:184px">
  <div class="panel-title">STARTING EXCHANGES</div>
  <p class="nolimit">No Limit</p>
  <ul class="list"><li class="hl">Zolvexa</li></ul>
</section>
<section class="abs panel" style="left:649px;top:556px;width:301px;height:179px">
  <div class="panel-title">ENDING EXCHANGES</div>
  <ul class="list">
    <li class="hl">Zolvexa</li><li>Kantriq</li><li>Fentaro</li><li>Yusken</li>
  </ul>
</section>
<a class="abs btn btn-primary" style="left:549px;top:791px;width:102px;height:29px;line-height:29px">NEXT</a>

<div class="abs divider" style="top:930px"></div>

<h2 class="abs h-center h-step" style="top:1000px">Step 2</h2>
<p class="abs sub" style="top:1046px">Please select your active &amp; Starting Coins</p>

<section class="abs panel" style="left:245px;top:1107px;width:306px;height:424px">
  <div class="panel-title">COIN LIST</div>
  <ul class="list">
    <li class="hl">KOVA<i class="toggle"></i></li>
    <li>MIRU<i class="toggle"></i></li>
    <li>UNIT<i class="toggle"></i></li>
    <li>UNITT<i class="toggle"></i></li>
    <li>BRIV<i class="off">x</i></li>
    <li>MIRU<i class="toggle"></i></li>
    <li>GLOM<i class="toggle"></i></li>
    <li>LUZE<i class="off">x</i></li>
    <li>EKTA<i class="toggle"></i></li>
    <li>ETRO<i class="toggle"></i></li>
    <li>AKTI<i class="toggle"></i></li>
    <li>DASQ<i class="off">x</i></li>
    <li>DIGO<i class="off">x</i></li>
  </ul>
</section>
<div class="abs arrow" style="left:592px;top:1166px">‹</div>
<div class="abs arrow" style="left:596px;top:1202px">›</div>
<div class="abs arrow" style="left:592px;top:1390px">‹</div>
<div class="abs arrow" style="left:596px;top:1426px">›</div>

<section class="abs panel" style="left:649px;top:1107px;width:301px;height:191px">
  <div class="panel-title">STARTING EXCHANGES</div>
  <p class="nolimit">No Limit</p>
  <ul class="list" style="padding-top:6px"><li class="hl">KOVA</li><li>MIRU</li><li>UNIT</li><li>BRIV</li></ul>
</section>
<section class="abs panel" style="left:649px;top:1322px;width:301px;height:201px">
  <div class="panel-title">ENDING EXCHANGES</div>
  <p class="nolimit">Limit</p>
  <ul class="list" style="padding-top:6px"><li class="dim">KOVA</li><li class="dim">MIRU</li><li class="dim">UNIT</li><li class="dim">BRIV</li></ul>
</section>
<a class="abs btn btn-primary" style="left:549px;top:1614px;width:102px;height:29px;line-height:29px">NEXT</a>

<section class="abs" style="left:147px;top:1807px;width:269px;height:153px;background:#fff">
  <div class="panel-title" style="margin:0">STEPS</div>
  <ul class="list" style="padding:8px 0 0">
    <li class="hl">Step 2<i class="toggle"></i></li>
    <li>Step 3<i class="off">x</i></li>
    <li>Step 4<i class="off">x</i></li>
    <li>Step 5<i class="off">x</i></li>
  </ul>
</section>
<section class="abs panel" style="left:458px;top:1807px;width:282px;height:153px">
  <h3 class="mp-title">Minimum Profit</h3>
  <div class="abs" style="left:84px;top:80px;font-size:10px">1.4%</div>
  <div class="slider"><i></i></div>
  <div class="abs" style="left:24px;top:116px;font-size:10px">0</div>
  <div class="abs" style="right:24px;top:116px;font-size:10px">Max</div>
</section>
<section class="abs" style="left:779px;top:1807px;width:274px;height:153px;background:#fff">
  <div class="panel-title" style="margin:0">WITHDRAW &amp; DEPOSIT STATUS</div>
  <ul class="status"><li><i class="dot"></i>Deposit Active</li><li><i class="dot"></i>Withdraw Active</li></ul>
</section>
<div class="abs radio" style="left:147px;top:1979px"><i class="dot"></i>All Available Steps</div>
<div class="abs radio" style="left:458px;top:1979px"><i class="dot" style="background:#cfe6f5;border-color:#e8f3fb"></i>Subscribe to Email Alerts</div>

<a class="abs btn btn-primary" style="left:421px;top:2055px;width:142px;height:35px;line-height:35px">SAVE FILTER</a>
<a class="abs btn btn-ghost" style="left:600px;top:2055px;width:176px;height:35px;line-height:33px">BACK TO FILTER</a>

<div class="abs divider" style="top:2197px"></div>

<h2 class="abs h-center h-step" style="top:2294px">Solutions</h2>
<section class="abs panel sol-table">
  <table>
    <thead><tr><th>Steps</th><th>Profit</th><th>Starting Exchanges</th><th>Ending Exchanges</th><th>Last Update</th><th>Withdraw / Deposit</th><th>Trade Details</th></tr></thead>
    <tbody>
      <tr class="hl"><td>3</td><td>5.4%</td><td>VINTOSKA</td><td>VINTOSKA</td><td>50 Sec</td><td>✓ / ✓</td><td><span class="det on">DETAILS</span></td></tr>
      <tr><td>3</td><td>4.4%</td><td>MOXELVANT</td><td>VINTOSKA</td><td>50 Sec</td><td>✓ / ✓</td><td><span class="det">DETAILS</span></td></tr>
      <tr><td>3</td><td>3.4%</td><td>DORVAK24</td><td>DORVAKCOIN</td><td>50 Sec</td><td>✓ / ✓</td><td><span class="det">DETAILS</span></td></tr>
      <tr><td>3</td><td>1.9%</td><td>PELZIQ</td><td>VINTOSKA</td><td>50 Sec</td><td>✓ / ✓</td><td><span class="det">DETAILS</span></td></tr>
      <tr><td>2</td><td>1.4%</td><td>VINTOSKA</td><td>BREMLOX</td><td>50 Sec</td><td>✓ / ✓</td><td><span class="det">DETAILS</span></td></tr>
      <tr><td>2</td><td>1.4%</td><td>BREMLOX</td><td>KANTRIQ</td><td>50 Sec</td><td>✓ / ✓</td><td><span class="det">DETAILS</span></td></tr>
      <tr><td>4</td><td>1.4%</td><td>VINTOSKA</td><td>ZOLVEXA</td><td>50 Sec</td><td>✓ / ✓</td><td><span class="det">DETAILS</span></td></tr>
      <tr><td>4</td><td>1.4%</td><td>ZOLVEXA</td><td>ZOLVEXA</td><td>50 Sec</td><td>✓ / ✓</td><td><span class="det">DETAILS</span></td></tr>
    </tbody>
  </table>
</section>
<svg class="abs chev" style="left:586px;top:2710px" width="28" height="16" viewBox="0 0 28 16"><path d="M3 3l11 10 11-10" fill="none" stroke="currentColor" stroke-width="3"/></svg>

<section class="abs panel detail">
  <table style="width:409px;margin:10px">
    <thead><tr><th>Steps</th><th>Profit</th><th style="text-align:right">Withdraw / Deposit</th></tr></thead>
    <tbody><tr><td>3</td><td>5.4%</td><td style="text-align:right">✓ / ✓</td></tr></tbody>
  </table>
  <div class="mini" style="top:98px"><table><thead><tr><th>Type</th><th>Asset</th><th>QTY</th><th>Price</th><th>Exchange</th><th></th></tr></thead>
    <tbody><tr><td>BUY</td><td>ZERV/KOVA</td><td>45.53 @</td><td>.0042</td><td>VINTOSKA</td><td class="link">Link to website</td></tr></tbody></table></div>
  <svg class="abs chev" style="left:206px;top:165px" width="16" height="10"><path d="M2 2l6 6 6-6" fill="none" stroke="currentColor" stroke-width="2"/></svg>
  <div class="transfer" style="top:196px">Transfer &nbsp;45.53 &nbsp;ZERV &nbsp;to &nbsp;Bremlox</div>
  <svg class="abs chev" style="left:206px;top:231px" width="16" height="10"><path d="M2 2l6 6 6-6" fill="none" stroke="currentColor" stroke-width="2"/></svg>
  <div class="mini" style="top:257px"><table><thead><tr><th>Type</th><th>Asset</th><th>QTY</th><th>Price</th><th>Exchange</th><th></th></tr></thead>
    <tbody><tr><td>SELL</td><td>ZERV/KOVA</td><td>45.53 @</td><td>.0047</td><td>BREMLOX</td><td class="link">Link to website</td></tr></tbody></table></div>
  <svg class="abs chev" style="left:206px;top:323px" width="16" height="10"><path d="M2 2l6 6 6-6" fill="none" stroke="currentColor" stroke-width="2"/></svg>
  <div class="transfer" style="top:355px">Transfer &nbsp;.2139 &nbsp;KOVA &nbsp;to &nbsp;VINTOSKA</div>
  <svg class="abs chev" style="left:206px;top:390px" width="16" height="10"><path d="M2 2l6 6 6-6" fill="none" stroke="currentColor" stroke-width="2"/></svg>
  <div class="mini" style="top:421px"><table><thead><tr><th>Type</th><th>Asset</th><th>QTY</th><th>Price</th><th>Exchange</th><th></th></tr></thead>
    <tbody><tr><td>SELL</td><td>KOVA/UNITT</td><td>.2139 @</td><td>5000</td><td>VINTOSKA</td><td class="link">Link to website</td></tr></tbody></table></div>
</section>

<footer class="abs site-footer">
  <div class="fcol" style="left:147px"><h4>Info</h4><ul><li>About Us</li><li>Fees</li><li>Promotions</li><li>Coin Metrics</li></ul></div>
  <div class="fcol" style="left:331px"><h4>Docs</h4><ul><li>User Agreement</li><li>Privacy Policy</li><li>API Documents</li></ul></div>
  <div class="fcol" style="left:539px"><h4>Support</h4><ul><li>Contact Us</li><li>FAQ's</li></ul></div>
  <div class="fcol social" style="left:715px"><h4>Media</h4><ul><li><i class="sq"></i>Chirper</li><li><i class="sq alt"></i>Lenscape</li></ul></div>
  <div class="abs flogo">QuillVex</div>
</footer>
<div class="abs bottom-bar">
  <span class="l">Users currently <b>online: 2614</b></span>
  <span class="r">Copyright © 2019 QuillVex. All Rights Reserved</span>
</div>

</body>
</html>
```